Debt Collection Website Design! We are the solution for landlords to get paid what they are owed.

We are a 3rd party debt collection company that specializes in Residential and Commercial real estate debt collection. We help landlords recover money from past residents by being fair, friendly and aggressive. We also collect/buy/sell/trade civil judgments won resulting from anything from automobile accidents to evictions to a pet zebra getting stolen. We buy single judgments to large portfolios, we also collect judgments for a nominal fee.

I would like a new, modern, easy to navigate website. A spot that we can post news stories or updated information about our company. I have included our company logo that must be on the top of the page. Feel free to ask any questions that will help get the process going.

Target Market(s)

Landlords, small to large apartment complex. Real estate services and lawyers.

Industry/Entity Type

Real Estate

Number of Pages Required

3 page

Requirements
Must have
• Company logo which has been attached. A page where we can explain the collection process, fees and placement. A page where we can explain judgments, collection vs. selling, placement form. I am open to any font/designs and willing to work with anyone.
Nice to have
• Nice to have a spot on the homepage to place news articles about ourselves and our industry.
Should not have
• I don't want it over crowded. Simple, sleek and easy to navigate is best. No gavels on any of the pages. It cannot look legal, say/show anything that we use legal powers to collect. We are not a law office, we don't practice law, we are 3rd party debt collection agency.

```html
<!DOCTYPE html>
<html lang="en">
<head>
<meta charset="utf-8">
<title>Halvorsen Recovery, LLC</title>
<link href="https://fonts.googleapis.com/css2?family=Cinzel:wght@400;600&family=Lato:ital,wght@0,400;0,700;1,400&display=swap" rel="stylesheet">
<style>
:root{
  --navy:#0b3a87;
  --navy-deep:#0a347c;
  --button-blue:#2d5fa9;
  --grey:#8e9196;
  --text:#333;
  --muted:#666;
  --line:#d7d9dd;
  --white:#fff;
}
*{box-sizing:border-box;margin:0;padding:0}
html,body{width:760px;height:1200px;overflow:hidden;background:var(--white)}
body{position:relative;font-family:"Lato",sans-serif;color:var(--text)}
.abs{position:absolute}

/* header */
.brand{left:54px;top:14px;display:flex;align-items:center;gap:10px}
.brand-mark{width:34px;height:34px;background:var(--navy)}
.brand-name{font-family:"Cinzel",serif;font-size:22px;line-height:22px;color:var(--navy);font-weight:400}
.brand-name small{display:block;font-size:14px;line-height:16px}
.top-phone{right:54px;top:9px;font-size:10px;color:var(--grey);letter-spacing:.5px;display:flex;align-items:center;gap:5px}
.nav{left:266px;top:32px;height:28px;display:flex;background:var(--navy);padding-right:24px;border-radius:0 14px 14px 0}
.nav a{display:block;color:var(--white);font-size:7.5px;font-weight:700;letter-spacing:.3px;text-decoration:none;line-height:28px;padding:0 11px;border-right:1px solid rgba(255,255,255,.15)}
.nav a.current{background:var(--grey)}

/* hero */
.hero{left:0;top:69px;width:760px;height:313px;background:linear-gradient(180deg,#3f78c4 0%,#7fa8d8 45%,#8b8f95 70%,#6c5446 100%)}
.hero-band{left:0;top:257px;width:378px;height:60px;background:rgba(25,25,25,.85);border-radius:0 30px 30px 0;padding:8px 0 0 56px}
.hero-band h1{font-family:"Cinzel",serif;font-weight:400;font-size:18px;line-height:22px;color:var(--white);letter-spacing:.5px}

/* section titles */
.sec-title{left:0;width:760px;text-align:center;font-family:"Cinzel",serif;font-size:18px;font-weight:400;color:var(--grey)}
.sec-title b{font-weight:400;color:var(--navy)}
.sec-title.on-dark{color:var(--white)}
.divider{left:237px;width:286px;height:10px}

/* about */
.about-lead{left:0;width:760px;top:456px;text-align:center;font-style:italic;font-size:8.5px;color:var(--muted)}
.about-body{left:92px;width:576px;top:475px;text-align:center;font-size:8px;line-height:14px;color:var(--text)}
.btn{background:var(--navy);color:var(--white);font-size:7.5px;font-weight:700;border-radius:2px;text-align:center}
.about-btn{left:342px;top:531px;width:60px;height:19px;line-height:19px}

/* properties */
.props{left:0;top:580px;width:760px;height:234px;background:linear-gradient(180deg,#2b3138,#1c2025)}
.card{top:653px;width:150px;height:137px;background:var(--white);padding:3px}
.card-img{width:144px;height:93px}
.card h3{font-size:8px;font-weight:700;margin:12px 0 0 7px;color:#222}
.card p{font-size:7.5px;color:var(--muted);margin:3px 0 0 7px}

/* news */
.news-img{top:901px;width:93px;height:82px}
.news-text{top:902px;width:220px}
.news-text time{font-size:6.5px;color:var(--text);display:block}
.news-text h3{font-size:8px;font-weight:700;margin-top:6px;color:#222}
.news-text p{font-size:7.5px;line-height:11px;color:var(--muted);margin-top:7px}
.news-text a{display:block;margin-top:7px;font-size:7.5px;font-weight:700;color:var(--navy);text-decoration:none}

/* footer */
.footer-rule{left:0;top:1025px;width:760px;height:3px;background:#aeb2b8}
.footer{left:0;top:1028px;width:760px;height:172px;background:var(--navy-deep);color:var(--white)}
.footer *{color:var(--white)}
.f-title{font-family:"Cinzel",serif;font-size:11px;font-weight:400;line-height:14px;padding-bottom:8px;border-bottom:1px solid rgba(255,255,255,.15)}
.f-col{top:22px}
.links{position:absolute;left:0;top:34px;list-style:none}
.links li{font-size:8px;line-height:13px;height:13px;padding-left:13px;position:relative;white-space:nowrap}
.links li::before{content:"›";position:absolute;left:1px;top:0}
.f-text{position:absolute;left:0;top:34px;font-size:8px;line-height:11px}
.contact-row{position:absolute;left:0;display:flex;align-items:center;gap:10px;font-size:8px;line-height:10px;white-space:nowrap}
.email-field{position:absolute;left:0;top:86px;width:149px;height:22px;background:var(--white);font-style:italic;font-size:6.5px;line-height:8px;color:#888;padding:7px 5px}
.footer .email-field{color:#888}
.sub-btn{position:absolute;left:0;top:116px;width:66px;height:23px;line-height:23px;background:var(--button-blue)}
.f-mark{left:624px;top:38px;width:40px;height:36px;background:rgba(255,255,255,.18)}
.social{left:596px;top:90px;display:flex;gap:6px}
.social span{width:20px;height:20px;background:var(--button-blue)}
.copy{left:560px;top:124px;width:146px;text-align:right;font-size:8px;line-height:11px}
</style>
</head>
<body>

<header>
  <div class="abs brand">
    <span class="brand-mark"></span>
    <div class="brand-name">Halvorsen<small>Recovery, LLC</small></div>
  </div>
  <div class="abs top-phone">
    <svg width="8" height="8" viewBox="0 0 10 10"><path d="M2 0.5 L3.8 2.8 L2.8 3.8 Q4 6 6.2 7.2 L7.2 6.2 L9.5 8 L8.3 9.5 Q3.5 9 0.5 1.7Z" fill="#8e9196"/></svg>
    555-204-1789
  </div>
  <nav class="abs nav">
    <a class="current">HOME</a><a>ABOUT</a><a>COMMERCIAL</a><a>RESIDENTIAL</a><a>PORTFOLIO</a><a>NEWS</a><a>CONTACT</a>
  </nav>
</header>

<section>
  <div class="abs hero" role="img" aria-label="Photo of a multi-storey apartment building with grey siding and brick under a blue sky"></div>
  <div class="abs hero-band"><h1>Residential &amp; Commercial<br>Real Estate Debt Collection.</h1></div>
</section>

<section>
  <h2 class="abs sec-title" style="top:409px">About <b>Halvorsen Recovery, LLC</b></h2>
  <svg class="abs divider" style="top:435px" viewBox="0 0 286 10"><line x1="0" y1="5" x2="124" y2="5" stroke="#d7d9dd"/><line x1="162" y1="5" x2="286" y2="5" stroke="#d7d9dd"/><circle cx="134" cy="5" r="2.5" fill="none" stroke="#bbb"/><circle cx="143" cy="5" r="3.2" fill="none" stroke="#bbb"/><circle cx="152" cy="5" r="2.5" fill="none" stroke="#bbb"/></svg>
  <p class="abs about-lead">Neque porro quisquam est qui dolorem ipsum quia dolor perspiciatis sit amet, consectetur,</p>
  <p class="abs about-body">Lorem ipsum dolor sit amet, consectetur adipiscing elit, sed do eiusmod tempor incididunt ut labore et dolore magna aliqua. Ut enim ad minim veniam, quis nostrud exercitation ullamco laboris nisi ut aliquip ex ea commodo consequat. Duis aute irure dolor in reprehenderit in voluptate velit esse cillum dolore eu fugiat nulla pariatur. Excepteur sint occaecat cupidatat non proident, sunt in culpa qui officia deserunt mollit anim id est laborum.</p>
  <div class="abs btn about-btn">Read more</div>
</section>

<section>
  <div class="abs props"></div>
  <h2 class="abs sec-title on-dark" style="top:601px">Latest Properties</h2>
  <svg class="abs divider" style="top:627px" viewBox="0 0 286 10"><line x1="0" y1="5" x2="124" y2="5" stroke="#555"/><line x1="162" y1="5" x2="286" y2="5" stroke="#555"/><circle cx="134" cy="5" r="2.5" fill="none" stroke="#777"/><circle cx="143" cy="5" r="3.2" fill="none" stroke="#777"/><circle cx="152" cy="5" r="2.5" fill="none" stroke="#777"/></svg>

  <div class="abs card" style="left:54px">
    <div class="card-img" role="img" aria-label="Photo of a modern white house with large windows at dusk" style="background:linear-gradient(180deg,#8fa9c4,#5d6b73 60%,#3b3f3a)"></div>
    <h3>Aliquam erat volutpat</h3><p>Aliquam dapibus and tincidunt</p>
  </div>
  <div class="abs card" style="left:222px">
    <div class="card-img" role="img" aria-label="Photo of a large suburban stone house with a double garage" style="background:linear-gradient(180deg,#3a6fc0,#9a8a78 55%,#5b7a3a)"></div>
    <h3>Mauris posuere</h3><p>Praesent justo lipsum dolor</p>
  </div>
  <div class="abs card" style="left:389px">
    <div class="card-img" role="img" aria-label="Photo of a grey two-storey house with a red door and garden" style="background:linear-gradient(180deg,#3c7ad0,#8a8c8e 50%,#3f6a30)"></div>
    <h3>Donec tempor libero</h3><p>Lobortis quis lobortis dignissim</p>
  </div>
  <div class="abs card" style="left:557px">
    <div class="card-img" role="img" aria-label="Photo of a red and stone family home with a driveway" style="background:linear-gradient(180deg,#2f64b8,#8a3a30 50%,#6e7a4a)"></div>
    <h3>Etiam dictum egestas</h3><p>Lorem ipsum dolor sit amet</p>
  </div>
</section>

<section>
  <h2 class="abs sec-title" style="top:841px">Latest <b>News</b></h2>
  <svg class="abs divider" style="top:867px" viewBox="0 0 286 10"><line x1="0" y1="5" x2="124" y2="5" stroke="#d7d9dd"/><line x1="162" y1="5" x2="286" y2="5" stroke="#d7d9dd"/><circle cx="134" cy="5" r="2.5" fill="none" stroke="#bbb"/><circle cx="143" cy="5" r="3.2" fill="none" stroke="#bbb"/><circle cx="152" cy="5" r="2.5" fill="none" stroke="#bbb"/></svg>

  <div class="abs news-img" style="left:54px;background:linear-gradient(135deg,#d9cfa8,#a88a5a 60%,#6f5d44)" role="img" aria-label="Photo of two people relaxing on a sofa at home"></div>
  <div class="abs news-text" style="left:158px">
    <time>March 02, 2015</time>
    <h3>Lorem ipsum cnonsnectetur aute irure dolor</h3>
    <p>Nemo enim ipsam voluptatem voluptas spernatur ut odit aut fugit, sed consequuntur magni dolores qui ratione voluptatem sequi nesciunt.</p>
    <a>Read more</a>
  </div>

  <div class="abs news-img" style="left:389px;background:linear-gradient(160deg,#5f7a3c,#c0623e 50%,#7a6a5c)" role="img" aria-label="Photo of suburban rooftops among trees"></div>
  <div class="abs news-text" style="left:493px">
    <time>March 02, 2015</time>
    <h3>Lorem ipsum cnonsnectetur aute irure dolor</h3>
    <p>Nemo enim ipsam voluptatem voluptas spernatur ut odit aut fugit, sed consequuntur magni dolores qui ratione voluptatem sequi nesciunt.</p>
    <a>Read more</a>
  </div>
</section>

<div class="abs footer-rule"></div>
<footer class="abs footer">
  <div class="abs f-col" style="left:54px;width:108px;height:140px">
    <h4 class="f-title">Quick Links</h4>
    <ul class="links">
      <li>Home</li><li>About</li><li>Commercial</li><li>Residential</li><li>Portfolio</li><li>News</li><li>Contact</li>
    </ul>
  </div>

  <div class="abs f-col" style="left:189px;width:128px;height:140px">
    <h4 class="f-title">Contact Detail</h4>
    <p class="f-text">16 Nemo enim ipsam vuptatem voluptas spe ut odit</p>
    <div class="contact-row" style="top:70px"><svg width="9" height="9" viewBox="0 0 10 10"><path d="M2 0.5 L3.8 2.8 L2.8 3.8 Q4 6 6.2 7.2 L7.2 6.2 L9.5 8 L8.3 9.5 Q3.5 9 0.5 1.7Z" fill="#fff"/></svg><span>555-204-1789</span></div>
    <div class="contact-row" style="top:93px"><svg width="9" height="9" viewBox="0 0 10 10"><rect x="2.5" y="0.5" width="5" height="3" fill="#fff"/><rect x="0.5" y="3.5" width="9" height="4" fill="#fff"/><rect x="2.5" y="6.5" width="5" height="3" fill="#fff" stroke="#0a347c" stroke-width=".6"/></svg><span>555-318-7890</span></div>
    <div class="contact-row" style="top:115px"><svg width="9" height="7" viewBox="0 0 10 7"><rect x="0.3" y="0.3" width="9.4" height="6.4" fill="#fff"/><path d="M0.3 0.3 L5 4 L9.7 0.3" fill="none" stroke="#0a347c" stroke-width=".8"/></svg><span>info@halvorsenrecovery.com</span></div>
  </div>

  <div class="abs f-col" style="left:377px;width:148px;height:140px">
    <h4 class="f-title">Newsletter Sign Up</h4>
    <p class="f-text">Lorem ipsudolor sit coec adipiscing elitsite amet</p>
    <div class="email-field">Email Address</div>
    <div class="btn sub-btn">Subscribe</div>
  </div>

  <div class="abs f-mark"></div>
  <div class="abs social"><span></span><span></span><span></span><span></span></div>
  <p class="abs copy">© 2014 Halvorsen Recovery, LLC<br>All Rights Reserved</p>
</footer>

</body>
</html>
```